Real eatate

My company name is “Maple Crest Realestate” i would like to create a business card. I would like something modern and sleek similar to picture uploaded. All text in the business card should be black and the logo gold any shade.

```html
<!DOCTYPE html>
<html lang="en">
<head>
<meta charset="UTF-8">
<title>Maple Crest Realestate – Business Card</title>
<link href="https://fonts.googleapis.com/css2?family=Montserrat:wght@400;500;700&display=swap" rel="stylesheet">
<style>
  :root {
    --backdrop: #b1b1ab;
    --card-light: #ffffff;
    --card-gold-soft: #efe3b0;
    --gold: #c9ad3a;
    --gold-deep: #b08f22;
    --ink: #111111;
  }
  * { margin: 0; padding: 0; box-sizing: border-box; }
  html, body {
    width: 1200px; height: 801px; overflow: hidden;
    background: var(--backdrop);
    font-family: "Montserrat", sans-serif;
    color: var(--ink);
  }
  .stage {
    position: relative; width: 1200px; height: 801px;
    display: flex; align-items: center; justify-content: center; gap: 40px;
  }
  .card {
    width: 540px; height: 309px; position: relative;
    box-shadow: 0 14px 30px rgba(0,0,0,0.22);
  }
  .card--front { background: var(--card-light); }
  .card--back {
    background: var(--card-gold-soft);
    display: flex; align-items: center; justify-content: center;
  }

  .brand { display: flex; align-items: center; gap: 12px; }
  .brand__mark { flex: none; background: var(--gold); }
  .brand__name {
    color: var(--ink); font-weight: 700; text-transform: uppercase;
    letter-spacing: 1px; line-height: 1.15;
  }

  .card--front .brand { position: absolute; left: 42px; top: 50%; transform: translateY(-50%); width: 230px; }
  .card--front .brand__mark { width: 18px; height: 18px; }
  .card--front .brand__name { font-size: 18px; }

  .card--back .brand__mark { width: 26px; height: 26px; background: var(--gold-deep); }
  .card--back .brand__name { font-size: 30px; }

  .divider {
    position: absolute; left: 290px; top: 98px; width: 1px; height: 113px;
    background: var(--gold);
  }
  .contact {
    position: absolute; left: 314px; top: 82px;
    color: var(--ink); font-size: 11.5px; line-height: 1.55;
  }
  .contact__name {
    font-size: 17px; font-weight: 500;
    letter-spacing: 1.5px; text-transform: uppercase; line-height: 1.2;
  }
  .contact__role { margin-bottom: 4px; }
  .contact__line { display: flex; align-items: center; gap: 6px; }
  .contact__icon { width: 9px; height: 9px; flex: none; }
</style>
</head>
<body>
<main class="stage">
  <section class="card card--front">
    <div class="brand">
      <span class="brand__mark"></span>
      <span class="brand__name">Maple Crest Realestate</span>
    </div>
    <span class="divider"></span>
    <div class="contact">
      <p class="contact__name">Daniel Harper</p>
      <p class="contact__role">Founder</p>
      <p>418 Birchwood Avenue</p>
      <p>Fairview, OR 97024</p>
      <p class="contact__line">
        <svg class="contact__icon" viewBox="0 0 10 10"><path d="M2 1l2 2-1 1.5c.6 1.2 1.3 1.9 2.5 2.5L7 6l2 2-1.3 1.3C4.5 9 1 5.5.7 2.3z" fill="#c9ad3a"/></svg>
        <span>555 210 4837</span>
      </p>
      <p class="contact__line">
        <svg class="contact__icon" viewBox="0 0 10 10"><rect x=".7" y="2" width="8.6" height="6" fill="none" stroke="#c9ad3a"/><path d="M.7 2L5 5.5 9.3 2" fill="none" stroke="#c9ad3a"/></svg>
        <span>info@maplecrest.com</span>
      </p>
      <p class="contact__line">
        <svg class="contact__icon" viewBox="0 0 10 10"><circle cx="5" cy="5" r="4.3" fill="none" stroke="#c9ad3a"/><path d="M.7 5h8.6M5 .7c-2 2.5-2 6 0 8.6M5 .7c2 2.5 2 6 0 8.6" fill="none" stroke="#c9ad3a" stroke-width=".7"/></svg>
        <span>www.maplecrest.com</span>
      </p>
    </div>
  </section>

  <section class="card card--back">
    <div class="brand">
      <span class="brand__mark"></span>
      <span class="brand__name">Maple Crest Realestate</span>
    </div>
  </section>
</main>
</body>
</html>
```